Diary toward Stillness - book cover

12/18 update: Please read the entire brief. I don’t love anything that has been provided up to today. Please use the graphics and colors I’ve attached!!!! Show me your creations.

I am looking for a book cover design. It is a mental health journal. Needs to be very warm, inviting, calming. I’m very interested in new creative ideas. It will be wire-o bound and also in hard copy front and back. Use the graphic and colors I already have attached to this file. It’s called “Diary Toward Stillness”. Self means soul or spirit or center. The idea of integration may be a fit here in some way. If some words need to be emphasized in the design, “Self” and “QMR” would be the most important. size 6"x9". The words on the front can be smaller and more inviting then they would normally be on a fiction paperback.

Update 12/16: I am not excited about any of the submissions so far. I’m looking forward to seeing more options.

Target Market(s)

Adults 30-60. Male and female. People who like to learn. People wanting to heal. Middle and upper income.

Industry/Entity Type

Mental health. Wellness

Other font styles liked:
• Whatever font is used in my logo. i don’t know the name. I also would be open to a different font if it was warm, inviting, and calm.

Colors
0094D4
00A9DD
6FCCEA
C7EBF8
E9F6FB

Requirements
Must have
• My logo colors. The words “Diary Toward Stillness” and “A 13-Week QMR Exploration”
Nice to have
• I’d like to see some creative ideas. More abstract than realistic.
Should not have
• No realist art or photos.

```html
<!DOCTYPE html>
<html lang="en">
<head>
<meta charset="UTF-8">
<title>Diary Toward Stillness – Book Cover</title>
<link rel="stylesheet" href="https://fonts.googleapis.com/css2?family=Playfair+Display:wght@400;600;700&family=Roboto+Condensed:wght@300&display=swap">
<style>
  :root {
    --blue-deep: #0094D4;
    --blue-bright: #00A9DD;
    --blue-sky: #6FCCEA;
    --blue-pale: #C7EBF8;
    --blue-mist: #E9F6FB;
    --ink: #1b5b6a;
    --ink-shadow: #0b3e4c;
    --stage: #e3eff3;
  }
  * { margin: 0; padding: 0; box-sizing: border-box; }
  html, body { width: 1200px; height: 800px; overflow: hidden; }
  body {
    background: var(--stage);
    display: flex;
    align-items: center;
    justify-content: center;
  }
  .cover {
    position: relative;
    width: 480px;
    height: 720px;
    background: linear-gradient(180deg, #eaf5fb 0%, var(--blue-mist) 100%);
    overflow: hidden;
    box-shadow: 0 6px 24px rgba(20, 70, 90, 0.15);
  }
  .hinge {
    position: absolute;
    left: 6px; top: 0; bottom: 0;
    width: 6px;
    border-left: 1px solid rgba(255,255,255,0.9);
    border-right: 1px solid rgba(150,190,210,0.35);
  }
  .block { position: absolute; }
  .block--top-left { left: 0; top: 0; width: 15%; height: 31%; background: rgba(199, 235, 248, 0.7); }
  .block--top-right { right: 0; top: 0; width: 19%; height: 30%; background: rgba(214, 233, 248, 0.8); }
  .block--bottom-left { left: 0; bottom: 0; width: 15%; height: 37%; background: linear-gradient(180deg, rgba(205,228,244,0.8), rgba(199,235,248,0.9)); }
  .block--bottom-right { right: 0; bottom: 0; width: 19%; height: 35%; background: rgba(199, 235, 248, 0.95); }

  .author {
    position: absolute;
    top: 26px; left: 0; right: 0;
    text-align: center;
    font-family: "Playfair Display", serif;
    font-variant: small-caps;
    font-size: 30px;
    letter-spacing: 4px;
    color: var(--ink);
  }
  .title {
    position: absolute;
    left: 0; right: 0;
    text-align: center;
    font-family: "Playfair Display", serif;
    font-weight: 600;
    color: var(--ink);
    text-shadow: -2px 2px 0 var(--ink-shadow);
    line-height: 1;
  }
  .title--main { top: 268px; font-size: 62px; transform: scaleX(0.86); }
  .title--self { top: 408px; font-size: 54px; transform: scaleX(0.86); }
  .connector {
    position: absolute;
    top: 362px; left: 0; right: 0;
    display: flex;
    align-items: center;
    justify-content: center;
    gap: 10px;
  }
  .connector__rule { width: 68px; height: 1.5px; background: var(--blue-bright); }
  .connector__text {
    font-family: "Roboto Condensed", sans-serif;
    font-weight: 300;
    font-size: 19px;
    color: var(--blue-bright);
  }
  .divider {
    position: absolute;
    top: 620px; left: 50%;
    width: 76px; height: 1px;
    margin-left: -38px;
    background: var(--ink);
  }
  .subtitle {
    position: absolute;
    top: 650px; left: 15%; right: 19%;
    width: auto;
    padding: 8px 0;
    background: rgba(199, 235, 248, 0.6);
    border: 2px solid rgba(255,255,255,0.85);
    text-align: center;
    font-family: "Playfair Display", serif;
    font-variant: small-caps;
    font-size: 17px;
    letter-spacing: 3px;
    color: var(--ink);
    white-space: nowrap;
  }
  .subtitle__key { font-weight: 700; }
</style>
</head>
<body>
  <main class="cover">
    <div class="block block--top-left"></div>
    <div class="block block--top-right"></div>
    <div class="block block--bottom-left"></div>
    <div class="block block--bottom-right"></div>
    <div class="hinge"></div>

    <p class="author">Author Name</p>

    <h1 class="title title--main">DIARY</h1>
    <div class="connector">
      <span class="connector__rule"></span>
      <span class="connector__text">TOWARD</span>
      <span class="connector__rule"></span>
    </div>
    <p class="title title--self">STILLNESS</p>

    <div class="divider"></div>
    <p class="subtitle">A 13-Week <span class="subtitle__key">QMR</span> Exploration</p>
  </main>
</body>
</html>
```